Wix web design for healthcare IT consulting firm.

I am looking for a web design built in Wix that it will be easy for me to add or edit content in the future. The web site does not need to be overly complicated, but it should look very polished and professional. I also want to ensure it is mobile device friendly. I do not need any type of on-line purchasing ability. I will eventually do blogs, but for now it is a fairly standard web site with main page, about us, services provided, etc. I would also like a place for potential customers to contact us directly from the web site. I have included a Word document with some content for the web design. I have also included my logo and business card for reference. I would like to utilize similar colors as my business card. One of my primary competitors is https://vonmarlhq.example/

Target Market(s)

Target market could be nursing home CEO, CIO, or other leader at an organization that manages long term care facilities.

Number of Pages Required

5+ page

Colors
876aae

Requirements
Must have
• Be designed to be used in Wix. Use the content I provided to create and make web design. Allow to be viewed on mobile device. Please use similar color structure as attached business card. Please use attached logo in design.

```html
<!DOCTYPE html>
<html lang="en">
<head>
<meta charset="utf-8">
<title>ClearPath – Healthcare IT Consulting</title>
<link rel="stylesheet" href="https://fonts.googleapis.com/css2?family=Open+Sans:wght@400;600;700&display=swap">
<style>
  :root{
    --brand:#876aae;
    --brand-deep:#6f4fa0;
    --panel-light:#9b74cc;
    --panel-dark:#8762bb;
    --hero-top:#7a56b0;
    --hero-bottom:#9a78c8;
    --ink:#3b3350;
    --muted:#9c98a6;
    --white:#ffffff;
    --strip:#f5f4f7;
  }
  *{box-sizing:border-box;margin:0;padding:0}
  html,body{width:1200px;height:686px;overflow:hidden;background:var(--white)}
  body{font-family:"Open Sans",Arial,sans-serif;color:var(--ink)}
  .page{position:relative;width:1200px;height:686px}

  .site-header{height:82px;display:flex;align-items:center;justify-content:space-between;padding:0 220px 0 222px;background:var(--white)}
  .brand{display:flex;align-items:center;gap:10px;font-weight:700;font-size:26px;color:var(--brand);letter-spacing:.5px}
  .brand-mark{width:14px;height:14px;background:var(--brand)}
  .main-nav{display:flex;gap:38px;font-size:11px;color:var(--muted)}
  .main-nav a{color:inherit;text-decoration:none}
  .main-nav a.is-active{color:var(--brand-deep);font-weight:600}

  .hero{position:relative;height:330px}
  .hero-photo{position:absolute;inset:0;background:linear-gradient(160deg,var(--hero-top) 0%,#8a68bd 45%,var(--hero-bottom) 100%)}
  .hero-quote{position:absolute;left:240px;top:206px;color:var(--white);font-weight:700;font-size:27px;line-height:1.02;text-transform:uppercase;letter-spacing:.2px}

  .contact-strip{height:80px;background:var(--strip);position:relative}
  .contact-item{position:absolute;top:24px;display:flex;align-items:center;gap:12px}
  .contact-item svg{flex:none}
  .contact-label{font-size:9px;color:var(--muted);margin-bottom:3px}
  .contact-value{font-size:13px;color:var(--ink)}
  .contact-line{width:134px;height:1px;background:var(--muted);margin-top:9px}

  .feature-row{position:absolute;left:226px;top:478px;display:flex;height:172px}
  .feature{display:flex;align-items:center;color:var(--white)}
  .feature--team{width:378px;background:var(--panel-light);padding:0 24px 0 28px;gap:26px}
  .feature--hours{width:380px;background:var(--panel-dark);padding:0 40px 0 34px;gap:30px}
  .feature-icon{flex:none;width:76px;height:66px;background:rgba(255,255,255,.35);border-radius:4px}
  .feature-title{font-weight:600;font-size:15px;margin-bottom:10px}
  .feature-text{font-size:8.5px;line-height:1.85;max-width:210px}
  .btn-more{display:inline-block;margin-top:12px;padding:5px 12px;border:1px solid rgba(255,255,255,.7);font-size:8px;color:var(--white);text-decoration:none}
  .hours-body{flex:1}
  .hours-table{width:100%;border-collapse:collapse;font-size:8px}
  .hours-table td{padding:8px 0;border-bottom:1px solid rgba(255,255,255,.35)}
  .hours-table td:last-child{text-align:right}
</style>
</head>
<body>
<div class="page">
  <header class="site-header">
    <div class="brand"><span class="brand-mark"></span>ClearPath</div>
    <nav class="main-nav">
      <a class="is-active" href="#">Home</a>
      <a href="#">About Us</a>
      <a href="#">Services Provided</a>
      <a href="#">Blog</a>
      <a href="#">Contact Us</a>
    </nav>
  </header>

  <section class="hero">
    <div class="hero-photo" role="img" aria-label="Purple-tinted photo of a stethoscope resting on a medical form"></div>
    <p class="hero-quote">“Increasing the value and<br>security of your<br>technology resources.”</p>
  </section>

  <section class="contact-strip">
    <div class="contact-item" style="left:226px">
      <svg width="14" height="22" viewBox="0 0 14 22" fill="none" stroke="#876aae" stroke-width="1.6"><rect x="1" y="1" width="12" height="20" rx="2"/><line x1="5" y1="17.5" x2="9" y2="17.5"/></svg>
      <div><div class="contact-label">Give us a Call</div><div class="contact-value">555-014-2290</div></div>
    </div>
    <div class="contact-item" style="left:472px">
      <svg width="22" height="16" viewBox="0 0 22 16" fill="none" stroke="#876aae" stroke-width="1.6"><rect x="1" y="1" width="20" height="14" rx="1.5"/><polyline points="1,2 11,9 21,2"/></svg>
      <div><div class="contact-label">Send us a Message</div><div class="contact-value">mreed@clearpathhc.example</div></div>
    </div>
    <div class="contact-item" style="left:727px">
      <svg width="16" height="22" viewBox="0 0 16 22" fill="none" stroke="#876aae" stroke-width="1.6"><path d="M8 21s7-8 7-13A7 7 0 0 0 1 8c0 5 7 13 7 13z"/><circle cx="8" cy="8" r="2.5"/></svg>
      <div><div class="contact-label">Visit our Location</div><div class="contact-line"></div></div>
    </div>
  </section>

  <section class="feature-row">
    <article class="feature feature--team">
      <div class="feature-icon" role="img" aria-label="Icon of a group of professionals"></div>
      <div>
        <h2 class="feature-title">Experienced Professionals</h2>
        <p class="feature-text">Led by a staff with a team of over 30 experienced professionals, ClearPath Healthcare is the trusted industry expert in Consulting and Healthcare Accounting.</p>
        <a class="btn-more" href="#">Read More</a>
      </div>
    </article>
    <article class="feature feature--hours">
      <svg width="68" height="68" viewBox="0 0 68 68" fill="none" stroke="#ffffff" stroke-width="2"><circle cx="34" cy="34" r="31"/><polyline points="34,16 34,34 46,40"/></svg>
      <div class="hours-body">
        <h2 class="feature-title">Opening Hours</h2>
        <table class="hours-table">
          <tr><td>Monday - Friday</td><td>8:30 - 17:00</td></tr>
          <tr><td>Monday - Friday</td><td>8:30 - 17:00</td></tr>
          <tr><td>Monday - Friday</td><td>8:30 - 17:00</td></tr>
        </table>
      </div>
    </article>
  </section>
</div>
</body>
</html>
```